Tervolan Pty Ltd professional business card

A professional business card template using the colours from the supplied logo.
Clean crisp lines while, Modern while not being over the top.

Target Market(s)

Construction, commerical and industrial

Industry/Entity Type

Communications

Contact Information for Business Card

For a Communications, IT, Optical fibre installation company

Colors
37b8a4

```html
<!DOCTYPE html>
<html lang="en">
<head>
<meta charset="utf-8">
<title>Tervolan Pty Ltd – Business Card</title>
<link rel="stylesheet" href="https://fonts.googleapis.com/css2?family=Open+Sans:wght@400;600&display=swap">
<style>
  :root {
    --teal: #37b8a4;
    --grey: #727276;
    --ink: #7c6a74;
    --edge: #1d8fb3;
    --backdrop: #2b2d31;
  }
  * { box-sizing: border-box; margin: 0; padding: 0; }
  html, body { width: 1200px; height: 900px; overflow: hidden; }
  body {
    background: var(--backdrop);
    font-family: "Open Sans", Arial, sans-serif;
    position: relative;
  }
  .card {
    position: absolute;
    left: 240px;
    width: 720px;
    height: 410px;
    border-radius: 22px;
    overflow: hidden;
    background: var(--grey);
  }
  .card--front { top: 27px; }
  .card--back { top: 463px; }
  .card__shapes { position: absolute; inset: 0; }

  .front__name {
    position: absolute;
    left: 0; right: 0; top: 160px;
    text-align: center;
    font-size: 76px;
    font-weight: 600;
    letter-spacing: 2px;
    color: var(--grey);
  }

  .back__name {
    position: absolute;
    left: 30px; top: 102px;
    width: 280px;
    text-align: center;
    font-size: 46px;
    font-weight: 600;
    color: var(--grey);
  }
  .holder {
    position: absolute;
    left: 480px; top: 158px;
    color: var(--ink);
  }
  .holder__name { font-size: 30px; font-weight: 600; line-height: 1.1; }
  .holder__role { font-size: 16px; text-align: right; }

  .contact-list {
    position: absolute;
    left: 258px; top: 262px;
    list-style: none;
    display: flex;
    flex-direction: column;
    gap: 4px;
  }
  .contact-list__item {
    display: flex;
    align-items: center;
    gap: 14px;
    min-height: 26px;
    font-size: 13px;
    line-height: 16px;
    color: var(--ink);
  }
  .contact-list__icon { width: 26px; height: 26px; flex: none; }
  .contact-list__rule {
    width: 30px;
    height: 2px;
    margin-left: 40px;
    background: var(--ink);
  }
</style>
</head>
<body>

<section class="card card--front" aria-label="Card front">
  <svg class="card__shapes" width="720" height="410" viewBox="0 0 720 410">
    <polygon points="70,0 690,0 650,410 30,410" fill="var(--teal)"/>
    <g fill="none" stroke="var(--edge)" stroke-width="5">
      <polyline points="175,40 140,80 175,120"/>
      <polyline points="205,40 170,80 205,120"/>
      <polyline points="235,40 200,80 235,120"/>
      <polyline points="485,290 520,330 485,370"/>
      <polyline points="515,290 550,330 515,370"/>
      <polyline points="545,290 580,330 545,370"/>
    </g>
  </svg>
  <div class="front__name">Tervolan</div>
</section>

<section class="card card--back" aria-label="Card back">
  <svg class="card__shapes" width="720" height="410" viewBox="0 0 720 410">
    <polygon points="0,40 290,40 330,135 290,230 0,230" fill="var(--teal)" stroke="var(--edge)" stroke-width="3"/>
    <polygon points="400,150 720,150 720,232 400,232 380,191" fill="var(--teal)" stroke="var(--edge)" stroke-width="3"/>
    <polygon points="260,250 720,250 720,412 230,412 230,290" fill="var(--teal)" stroke="var(--edge)" stroke-width="3"/>
    <circle cx="435" cy="191" r="22" fill="none" stroke="var(--ink)" stroke-width="2.5"/>
    <circle cx="435" cy="184" r="7" fill="none" stroke="var(--ink)" stroke-width="2.5"/>
    <path d="M422 203 q13 -14 26 0" fill="none" stroke="var(--ink)" stroke-width="2.5"/>
  </svg>

  <div class="back__name">Tervolan</div>

  <div class="holder">
    <div class="holder__name">Lorem ipsum</div>
    <div class="holder__role">Designer</div>
  </div>

  <ul class="contact-list">
    <li class="contact-list__item">
      <svg class="contact-list__icon" viewBox="0 0 26 26"><circle cx="13" cy="13" r="13" fill="var(--grey)"/><path d="M7 13 L13 7 L19 13 M9 12 V19 H17 V12" fill="none" stroke="var(--teal)" stroke-width="2"/></svg>
      <span>14 Harbour Road<br>Perth WA 6000</span>
    </li>
    <li class="contact-list__rule" aria-hidden="true"></li>
    <li class="contact-list__item">
      <svg class="contact-list__icon" viewBox="0 0 26 26"><circle cx="13" cy="13" r="13" fill="var(--grey)"/><path d="M7 13 L19 7 L15 19 L13 14 Z" fill="var(--teal)"/></svg>
      <span>hello@tervolan-mail.com</span>
    </li>
    <li class="contact-list__rule" aria-hidden="true"></li>
    <li class="contact-list__item">
      <svg class="contact-list__icon" viewBox="0 0 26 26"><circle cx="13" cy="13" r="13" fill="var(--grey)"/><path d="M9 7 L12 10 L10 12 Q12 15 14 16 L16 14 L19 17 L17 19 Q10 18 7 9 Z" fill="var(--teal)"/></svg>
      <span>+61 8 5550 1234<br>+61 4 5550 9876</span>
    </li>
    <li class="contact-list__rule" aria-hidden="true"></li>
    <li class="contact-list__item">
      <svg class="contact-list__icon" viewBox="0 0 26 26"><circle cx="13" cy="13" r="13" fill="var(--grey)"/><circle cx="13" cy="13" r="6" fill="none" stroke="var(--teal)" stroke-width="1.6"/><path d="M7 13 H19 M13 7 Q9 13 13 19 Q17 13 13 7" fill="none" stroke="var(--teal)" stroke-width="1.4"/></svg>
      <span>www.tervolan-net.com</span>
    </li>
  </ul>
</section>

</body>
</html>
```